Photography blog homepage design

I need a new webpage design for my photography blog. My blog focuses on post-processing techniques, particularly in luminosity masking, HDR photography and other advanced photo editing skills. I want the new homepage to let visitors know instantly what the blog is about as this is currently not very obvious from the feedback I received. Apart from that, the homepage should also inform/showcase latest blog post and/or popular blog post and/or some of the training courses I offer (that's my idea, but I leave it to your expertise). There should also ideally have a CTA that leads visitors to the "Start Here" page where they can learn more about my blog. The bulk of my audience is intermediate/advanced photographers who are above 30-35 years old, with a significant group in the 60 to >75 age group. The design should convey trust and creativity at the same time. The color theme for my blog is orange and dark grey. URL is www.lumivarnic.com, you can use the current content on that page.

Target Market(s)

Intermediate/advanced photographers (hobbyist or professional) age 35-75 years old.

Number of Pages Required

1 page

Font styles to use
Sans Serif

Colors
faa54b
f68e4e
f78f20

Requirements
Must have
• Upside down homepage (menus at the bottom)

```html
<!DOCTYPE html>
<html lang="en">
<head>
<meta charset="utf-8">
<title>Lumivarnic – Photography Blog</title>
<link rel="stylesheet" href="https://fonts.googleapis.com/css2?family=Open+Sans:wght@400;600;700;800&family=Roboto+Slab:wght@300;400&display=swap">
<style>
:root{
  --orange:#f78f20;
  --orange-soft:#faa54b;
  --orange-mid:#f68e4e;
  --dark:#333333;
  --text:#555555;
  --muted:#9a9a9a;
  --line:#e6e6e6;
  --bg:#ffffff;
}
*{box-sizing:border-box;margin:0;padding:0}
html,body{width:1200px;height:3172px;overflow:hidden}
body{background:var(--bg);font-family:"Open Sans",Arial,sans-serif;color:var(--text);position:relative}
h1,h2,h3{font-weight:400}

/* header */
.topbar{height:40px;display:flex;justify-content:space-between;align-items:center;padding:0 24px;font-size:11px;color:var(--dark)}
.social{display:flex;gap:6px}
.social span{width:16px;height:16px;border-radius:50%;background:var(--orange);display:block}
.logo{position:absolute;top:18px;left:0;right:0;text-align:center;font-weight:800;font-size:40px;letter-spacing:1px;color:var(--dark);line-height:48px}
.logo::before{content:"";display:inline-block;width:14px;height:14px;border-radius:50%;background:var(--orange);margin-right:10px;vertical-align:middle}
.header-tools{position:absolute;top:78px;right:170px;display:flex;gap:10px;align-items:center}
.search{width:150px;height:22px;border:1px solid var(--line);border-radius:2px;font-size:10px;color:var(--muted);padding:4px 8px;line-height:12px}
.start-btn{width:56px;height:22px;background:var(--orange-soft);color:#fff;font-size:10px;font-weight:700;text-align:center;line-height:22px;border-radius:2px}

/* hero */
.hero{position:absolute;top:112px;left:0;width:1200px;height:388px;background:linear-gradient(180deg,#7a8aa6 0%,#e8a070 45%,#5a4a52 75%,#2c2a34 100%)}
.hero-title{position:absolute;top:130px;left:0;right:0;text-align:center;font-weight:800;font-size:96px;line-height:120px;color:#fff;letter-spacing:4px}
.hero-arrow{position:absolute;top:178px;width:26px;height:30px;background:rgba(0,0,0,.55)}
.hero-arrow.left{left:0}.hero-arrow.right{right:0}

/* post grid */
.grid{position:absolute;top:568px;left:168px;width:864px;display:grid;grid-template-columns:repeat(3,272px);gap:32px 24px}
.card{background:#fff;box-shadow:0 1px 6px rgba(0,0,0,.12);height:400px}
.card .photo{height:168px}
.card .body{padding:14px}
.cat{color:var(--orange);font-size:10px;margin-bottom:8px}
.title{font-family:"Roboto Slab",Georgia,serif;font-weight:400;font-size:17px;line-height:22px;color:var(--dark);margin-bottom:10px}
.excerpt{font-size:10px;line-height:15px;color:var(--muted);margin-bottom:14px}
.more{color:var(--orange);font-size:9px;text-decoration:underline;display:block}
.date{font-size:9px;color:var(--dark);margin-top:2px}

/* featured list */
.list{position:absolute;top:1520px;left:168px;width:572px}
.item{display:flex;gap:18px;height:256px}
.item .photo{width:140px;height:214px;flex:none}
.item .title{font-size:20px;line-height:26px}
.item .body{padding-top:4px;width:300px}

/* sidebar */
.side{position:absolute;top:1508px;left:760px;width:272px}
.side h3{font-size:12px;color:var(--dark);font-weight:600;margin-bottom:10px}
.trend{display:flex;align-items:center;gap:14px;height:60px;padding:0 14px;border:1px solid var(--line);margin-bottom:6px;font-size:10px;color:var(--dark)}
.trend b{font-size:18px;font-weight:700}
.trend.hot{background:var(--orange-soft);color:#fff;border:none;height:110px}
.recent{display:flex;gap:12px;align-items:center;height:50px;margin-bottom:10px;font-size:10px;color:var(--dark)}
.recent .photo{width:48px;height:44px;flex:none}
.recent small{display:block;color:var(--muted);font-size:9px}

/* news */
.section-title{position:absolute;left:0;right:0;text-align:center;font-family:"Roboto Slab",Georgia,serif;font-weight:300;font-size:30px;line-height:40px;color:var(--dark)}
.news{position:absolute;top:2380px;left:-128px;display:flex;gap:24px}
.news-card{width:272px;height:380px;background:#fff;box-shadow:0 1px 6px rgba(0,0,0,.12)}
.news-card .photo{height:210px}
.news-card .body{padding:14px 20px}
.news-card .title{font-size:15px;line-height:19px;text-align:center}
.btn{display:block;width:96px;margin:8px auto 0;background:var(--orange);color:#fff;font-size:10px;font-weight:700;text-align:center;padding:6px 0}
.strip{position:absolute;top:2848px;left:0;width:1200px;height:92px;display:flex}
.strip div{flex:1}

/* footer with menu at the bottom */
.foot-logo{position:absolute;top:2968px;left:0;right:0;text-align:center;font-weight:800;font-size:34px;line-height:44px;color:var(--dark)}
.foot-logo::before{content:"";display:inline-block;width:12px;height:12px;border-radius:50%;background:var(--orange);margin-right:10px;vertical-align:middle}
.foot-social{position:absolute;top:3020px;left:0;right:0;display:flex;justify-content:center;gap:10px}
.foot-social span{width:22px;height:22px;border-radius:50%;background:var(--orange)}
.nav{position:absolute;top:3062px;left:0;right:0;height:36px;background:var(--orange);display:flex;align-items:center;justify-content:center}
.nav ul{list-style:none;display:flex;gap:28px}
.nav li{color:#fff;font-size:11px;font-weight:600;line-height:16px}
.nav li.active{border-bottom:2px solid #fff}
.copy{position:absolute;top:3120px;left:0;right:0;text-align:center;font-size:10px;color:var(--muted)}
</style>
</head>
<body>

<header>
  <div class="topbar"><span>Privacy Policy | Contact</span><div class="social"><span></span><span></span><span></span><span></span><span></span></div></div>
  <div class="logo">LUMIVARNIC</div>
  <div class="header-tools"><div class="search">Search</div><div class="start-btn">START</div></div>
</header>

<section class="hero" role="img" aria-label="Domed capitol building under a sunset sky">
  <div class="hero-title">LUMIVARNIC</div>
  <div class="hero-arrow left"></div><div class="hero-arrow right"></div>
</section>

<section class="grid">
  <article class="card"><div class="photo" role="img" aria-label="Sunset over a rocky coast" style="background:linear-gradient(#e6a46a,#6a4a3a)"></div><div class="body"><p class="cat">Post-Processing Techniques</p><h2 class="title">I am a blogger living in New York. This is my blog.</h2><p class="excerpt">Lorem ipsum is simply dummy text of the printing and typesetting industry, used since long ago.</p><a class="more">Continue reading</a><p class="date">May 6, 2016</p></div></article>
  <article class="card"><div class="photo" role="img" aria-label="Golden light on a mountain valley" style="background:linear-gradient(#d8a060,#5a4030)"></div><div class="body"><p class="cat">HDR Photography</p><h2 class="title">I am a blogger living in New York. This is my blog.</h2><p class="excerpt">Lorem ipsum is simply dummy text of the printing and typesetting industry, used since long ago.</p><a class="more">Continue reading</a><p class="date">May 6, 2016</p></div></article>
  <article class="card"><div class="photo" role="img" aria-label="Lake at dusk below distant hills" style="background:linear-gradient(#8aa0b8,#3a3a48)"></div><div class="body"><p class="cat">Introduction to Luminosity Masking</p><h2 class="title">I am a blogger living in New York. This is my blog.</h2><p class="excerpt">Lorem ipsum is simply dummy text of the printing and typesetting industry, used since long ago.</p><a class="more">Continue reading</a><p class="date">May 6, 2016</p></div></article>
  <article class="card"><div class="photo" role="img" aria-label="Figure on a beach at sunset" style="background:linear-gradient(#5fa8d0,#d89860)"></div><div class="body"><p class="cat">HDR Photography</p><h2 class="title">I am a blogger living in New York. This is my blog.</h2><p class="excerpt">Lorem ipsum is simply dummy text of the printing and typesetting industry, used since long ago.</p><a class="more">Continue reading</a><p class="date">May 6, 2016</p></div></article>
  <article class="card"><div class="photo" role="img" aria-label="Snowy mountain peaks at dawn" style="background:linear-gradient(#6a7aa0,#2a3040)"></div><div class="body"><p class="cat">Post-Processing Techniques</p><h2 class="title">I am a blogger living in New York. This is my blog.</h2><p class="excerpt">Lorem ipsum is simply dummy text of the printing and typesetting industry, used since long ago.</p><a class="more">Continue reading</a><p class="date">May 6, 2016</p></div></article>
  <article class="card"><div class="photo" role="img" aria-label="Red cliffs under an evening sky" style="background:linear-gradient(#c07050,#4a2a28)"></div><div class="body"><p class="cat">Introduction to Luminosity Masking</p><h2 class="title">I am a blogger living in New York. This is my blog.</h2><p class="excerpt">Lorem ipsum is simply dummy text of the printing and typesetting industry, used since long ago.</p><a class="more">Continue reading</a><p class="date">May 6, 2016</p></div></article>
</section>

<section class="list">
  <article class="item"><div class="photo" role="img" aria-label="Glass pyramid building" style="background:linear-gradient(#b8c4cc,#6a7880)"></div><div class="body"><p class="cat">HDR Photography</p><h2 class="title">Find Your Best topic?</h2><p class="excerpt">Lorem ipsum is simply dummy text of the printing and typesetting industry. Lorem ipsum has been the industry's standard dummy text ever since the 1500s, when an unknown printer took a galley.</p><a class="more">Continue reading</a><p class="date">May 6, 2016</p></div></article>
  <article class="item"><div class="photo" role="img" aria-label="Waterfall over dark rocks" style="background:linear-gradient(#8a9aa0,#3a4038)"></div><div class="body"><p class="cat">Introduction to Luminosity Masking</p><h2 class="title">Find Your Best topic?</h2><p class="excerpt">Lorem ipsum is simply dummy text of the printing and typesetting industry. Lorem ipsum has been the industry's standard dummy text ever since the 1500s, when an unknown printer took a galley.</p><a class="more">Continue reading</a><p class="date">May 6, 2016</p></div></article>
  <article class="item"><div class="photo" role="img" aria-label="Sea rocks glowing at sunset" style="background:linear-gradient(#f0a050,#6a3a20)"></div><div class="body"><p class="cat">Post-Processing Techniques</p><h2 class="title">Find Your Best topic?</h2><p class="excerpt">Lorem ipsum is simply dummy text of the printing and typesetting industry. Lorem ipsum has been the industry's standard dummy text ever since the 1500s, when an unknown printer took a galley.</p><a class="more">Continue reading</a><p class="date">May 6, 2016</p></div></article>
</section>

<aside class="side">
  <h3>Trending Now</h3>
  <div class="trend hot"><b>01</b><span>Describe the world with one<br>May 10, 2016</span></div>
  <div class="trend"><b>02</b><span>Describe the world with one</span></div>
  <div class="trend"><b>03</b><span>Describe the world with one</span></div>
  <h3 style="margin-top:18px">Recently Posted</h3>
  <div class="recent"><div class="photo" role="img" aria-label="Sunset landscape" style="background:linear-gradient(#e89050,#4a3028)"></div><span>You Can do Anything<small>May 6, 2016</small></span></div>
  <div class="recent"><div class="photo" role="img" aria-label="Mountain lake" style="background:linear-gradient(#7a98b0,#3a4a50)"></div><span>You Can do Anything<small>May 6, 2016</small></span></div>
  <div class="recent"><div class="photo" role="img" aria-label="Coastline" style="background:linear-gradient(#a0b0c0,#4a5058)"></div><span>You Can do Anything<small>May 6, 2016</small></span></div>
  <div class="recent"><div class="photo" role="img" aria-label="Evening valley" style="background:linear-gradient(#9a8070,#3a3030)"></div><span>You Can do Anything<small>May 6, 2016</small></span></div>
</aside>

<h2 class="section-title" style="top:2314px">News &amp; Updates</h2>
<section class="news">
  <article class="news-card"><div class="photo" role="img" aria-label="Temple at sunset" style="background:linear-gradient(#e0a060,#4a3a30)"></div><div class="body"><h3 class="title">Lorem Ipsum Is Simply Dummy Text Of Printing</h3><span class="btn">READ MORE</span></div></article>
  <article class="news-card"><div class="photo" role="img" aria-label="Rocky shore under clouds" style="background:linear-gradient(#8a98a8,#2a3038)"></div><div class="body"><h3 class="title">Lorem Ipsum Is Simply Dummy Text Of Printing</h3><span class="btn">READ MORE</span></div></article>
  <article class="news-card"><div class="photo" role="img" aria-label="Dramatic sunset over water" style="background:linear-gradient(#f0a050,#5a3a30)"></div><div class="body"><h3 class="title">Lorem Ipsum Is Simply Dummy Text Of Printing</h3><span class="btn">READ MORE</span></div></article>
  <article class="news-card"><div class="photo" role="img" aria-label="Old red truck in a field" style="background:linear-gradient(#98a8b0,#8a4a30)"></div><div class="body"><h3 class="title">Lorem Ipsum Is Simply Dummy Text Of Printing</h3><span class="btn">READ MORE</span></div></article>
  <article class="news-card"><div class="photo" role="img" aria-label="Couple in a sunny meadow" style="background:linear-gradient(#e8c890,#7a8050)"></div><div class="body"><h3 class="title">Lorem Ipsum Is Simply Dummy Text Of Printing</h3><span class="btn">READ MORE</span></div></article>
</section>

<h2 class="section-title" style="top:2790px">Follow me @Lumivarnic</h2>
<section class="strip" role="img" aria-label="Row of recent landscape photographs">
  <div style="background:#c07a48"></div><div style="background:#4a5a68"></div><div style="background:#8a9aa8"></div><div style="background:#e09a50"></div><div style="background:#5a7a58"></div><div style="background:#3a5868"></div><div style="background:#d8a868"></div><div style="background:#6a8a70"></div><div style="background:#a86a48"></div>
</section>

<footer>
  <div class="foot-logo">LUMIVARNIC</div>
  <div class="foot-social"><span></span><span></span><span></span><span></span><span></span></div>
  <nav class="nav">
    <ul><li class="active">HOME</li><li>ABOUT</li><li>SERVICES</li><li>BLOG</li><li>CONTACT</li></ul>
  </nav>
  <p class="copy">© Lumivarnic 2016. All rights reserved.</p>
</footer>

</body>
</html>
```